5 year service award card*

I'm attaching a celebration type card in which I need a new card similar made but with VRK logo's on it instead.

Colors

Designer to choose colors to be used in the design.

```html
<!DOCTYPE html>
<html lang="en">
<head>
<meta charset="utf-8">
<title>VRK 5 Year Anniversary Card</title>
<link rel="stylesheet" href="https://fonts.googleapis.com/css2?family=Cinzel:wght@400&family=Quicksand:wght@300;400;500&display=swap">
<style>
  :root {
    --page-bg: #f2f2f2;
    --card-bg: #ffffff;
    --gold: #c49a45;
    --gold-light: #e8c877;
    --gold-dark: #9a7126;
    --gold-text: #c8a05a;
    --ink: #2b2b2b;
    --ink-blue: #2b54a8;
  }
  * { box-sizing: border-box; margin: 0; padding: 0; }
  html, body { width: 927px; height: 1200px; overflow: hidden; background: var(--page-bg); }
  .award-card {
    position: absolute; left: 83px; top: 12px;
    width: 760px; height: 1176px;
    background: var(--card-bg);
  }
  .frame { position: absolute; left: 0; top: 0; }
  .corner-ornament {
    position: absolute; width: 104px; height: 104px;
    background: radial-gradient(circle at 35% 35%, var(--gold-light), var(--gold) 55%, var(--gold-dark));
    opacity: .85;
  }
  .corner-ornament.tl { left: 38px; top: 40px; border-radius: 0 0 70% 0; }
  .corner-ornament.tr { right: 38px; top: 40px; border-radius: 0 0 0 70%; }
  .corner-ornament.bl { left: 38px; bottom: 40px; border-radius: 0 70% 0 0; }
  .corner-ornament.br { right: 38px; bottom: 40px; border-radius: 70% 0 0 0; }
  .heading { position: absolute; left: 0; top: 120px; width: 760px; height: 240px; }
  .message {
    position: absolute; left: 110px; top: 396px; width: 540px;
    font-family: "Quicksand", sans-serif; font-weight: 400;
    font-size: 27px; line-height: 38px; text-align: center;
    color: var(--gold-text);
  }
  .date-rule { position: absolute; left: 182px; width: 412px; height: 3px; background: var(--gold); }
  .date-rule.top { top: 656px; }
  .date-rule.bottom { top: 782px; }
  .date-row {
    position: absolute; left: 182px; top: 659px; width: 412px; height: 123px;
    font-family: "Quicksand", sans-serif; color: var(--gold-text);
  }
  .date-month, .date-year { position: absolute; top: 46px; font-size: 27px; font-weight: 400; letter-spacing: 1px; line-height: 32px; }
  .date-month { left: 44px; }
  .date-year { right: 46px; }
  .date-day { position: absolute; left: 0; width: 412px; top: 0; text-align: center; font-size: 108px; font-weight: 400; line-height: 123px; }
  .signatures {
    position: absolute; left: 172px; top: 804px; width: 432px; height: 244px;
    background: linear-gradient(160deg, rgba(43,43,43,.08), rgba(43,84,168,.10));
    border-radius: 8px;
  }
  .brand {
    position: absolute; left: 0; width: 760px; top: 1060px; height: 44px;
    display: flex; justify-content: center; align-items: center;
    font-family: "Quicksand", sans-serif; font-weight: 500;
    font-size: 38px; line-height: 44px; letter-spacing: 4px; color: var(--gold-text);
  }
</style>
</head>
<body>
<main class="award-card">
  <svg class="frame" width="760" height="1176" viewBox="0 0 760 1176" aria-hidden="true">
    <g fill="none" stroke="#c49a45">
      <line x1="150" y1="47" x2="610" y2="47" stroke-width="4"/>
      <line x1="150" y1="55" x2="610" y2="55" stroke-width="1.5"/>
      <line x1="150" y1="1129" x2="610" y2="1129" stroke-width="4"/>
      <line x1="150" y1="1121" x2="610" y2="1121" stroke-width="1.5"/>
      <line x1="50" y1="155" x2="50" y2="1021" stroke-width="4"/>
      <line x1="60" y1="155" x2="60" y2="1021" stroke-width="1.5"/>
      <line x1="710" y1="155" x2="710" y2="1021" stroke-width="4"/>
      <line x1="700" y1="155" x2="700" y2="1021" stroke-width="1.5"/>
    </g>
  </svg>
  <div class="corner-ornament tl" role="img" aria-label="Gold baroque corner ornament"></div>
  <div class="corner-ornament tr" role="img" aria-label="Gold baroque corner ornament"></div>
  <div class="corner-ornament bl" role="img" aria-label="Gold baroque corner ornament"></div>
  <div class="corner-ornament br" role="img" aria-label="Gold baroque corner ornament"></div>

  <svg class="heading" width="760" height="240" viewBox="0 0 760 240">
    <defs>
      <linearGradient id="headingGold" x1="0" y1="0" x2="1" y2="1">
        <stop offset="0" stop-color="#e3bf6c"/>
        <stop offset=".5" stop-color="#c49a45"/>
        <stop offset="1" stop-color="#a87c2c"/>
      </linearGradient>
      <path id="anniversaryArc" d="M185 95 Q380 -5 600 95"/>
    </defs>
    <g font-family="Cinzel, serif" fill="url(#headingGold)" text-anchor="middle">
      <text font-size="50" letter-spacing="1"><textPath href="#anniversaryArc" startOffset="50%">ANNIVERSARY</textPath></text>
      <text x="380" y="163" font-size="80">5</text>
      <text x="380" y="230" font-size="72" letter-spacing="4">YEAR</text>
    </g>
  </svg>

  <p class="message">Thank you for being part of our<br>company,s success over these 5<br>years.&nbsp; we greatly appreiate and<br>value your hard worh and<br>commitment to making it work right<br>the first time.</p>

  <div class="date-rule top"></div>
  <div class="date-row">
    <span class="date-month">NOV</span>
    <span class="date-day">28</span>
    <span class="date-year">2019</span>
  </div>
  <div class="date-rule bottom"></div>

  <div class="signatures" role="img" aria-label="Handwritten team signatures in black and blue ink"></div>

  <div class="brand"><span class="brand-name">VRK</span></div>
</main>
</body>
</html>
```